EPIC, awesome, creative business card needed - get involved!

I'm launching a boutique, exclusive Property Management real estate agency in Sydney early next year.
The name of the agency will be called "Quartz Hill Lane" - it's a play on "chase the silver pebble trail" to wealth. The Quartz Hill Lane signifies wealth through property investment.
My business will offer management of investment properties (ie Property Management).
The difference with Quartz Hill Lane and other agencies is the business will be run by one of Australia's leading property investment experts, and also one of Australia's leading property managers.
It will be exclusively for high net worth properties and individuals, so the business card needs to be extremely sharp, slick and relatively simple.
The information I want on the card is as follows
Nolan Pryce - Director
M: 0412 967 154
P: 9735 6021
E: nolan@quartzhilllane.net.au
W: quartzhilllane.net.au
I'm happy with the red from the logo, black - no yellows or funky colors. I want this to be a super corporate and slick business card to match the high end nature of the business.
Good luck everyone, and please ask questions for clarification.

```html
<!DOCTYPE html>
<html lang="en">
<head>
<meta charset="utf-8">
<title>Quartz Hill Lane – Business Card</title>
<link rel="stylesheet" href="https://fonts.googleapis.com/css2?family=Open+Sans:wdth,wght@75..100,400..800&display=swap">
<style>
  :root {
    --brand-red: #c4242b;
    --card-black: #000000;
    --ink-white: #ffffff;
    --page-bg: #ffffff;
  }
  * { margin: 0; padding: 0; box-sizing: border-box; }
  html, body {
    width: 1200px;
    height: 2398px;
    overflow: hidden;
    background: var(--page-bg);
    font-family: "Open Sans", Arial, sans-serif;
  }
  .condensed { font-stretch: 75%; font-weight: 700; }

  .card {
    position: absolute;
    background: var(--card-black);
    border-radius: 32px;
    overflow: hidden;
  }
  .card--front { left: 90px; top: 208px; width: 1020px; height: 568px; }
  .card--back  { left: 88px; top: 936px; width: 1022px; height: 568px; }

  /* Front */
  .front-brand {
    position: absolute;
    left: 76px;
    top: 384px;
    display: flex;
    align-items: center;
    gap: 18px;
  }
  .front-brand-mark {
    width: 52px;
    height: 52px;
    background: var(--brand-red);
    flex: none;
  }
  .front-brand-name {
    color: var(--brand-red);
    font-size: 46px;
    line-height: 1;
  }
  .front-web {
    position: absolute;
    right: 76px;
    top: 480px;
    color: var(--brand-red);
    font-size: 33px;
    line-height: 1;
  }

  /* Back */
  .band {
    position: absolute;
    background: var(--brand-red);
    top: 220px;
    height: 136px;
  }
  .band--brand {
    left: 0;
    width: 178px;
    display: flex;
    align-items: center;
    justify-content: center;
  }
  .band--name  { left: 644px; width: 378px; }

  .band-brand-name {
    color: var(--ink-white);
    font-size: 20px;
    line-height: 1;
    white-space: nowrap;
  }

  .contact-list {
    position: absolute;
    left: 226px;
    top: 236px;
    list-style: none;
    color: var(--ink-white);
    font-size: 28px;
    line-height: 37px;
  }
  .contact-list li { display: flex; align-items: center; }
  .contact-list li::before {
    content: "";
    width: 20px;
    height: 20px;
    background: var(--brand-red);
    margin-right: 26px;
    flex: none;
  }

  .person {
    position: absolute;
    right: 82px;
    top: 22px;
    text-align: right;
    color: var(--ink-white);
  }
  .person-name {
    font-size: 44px;
    font-weight: 600;
    letter-spacing: 2px;
    line-height: 1.1;
  }
  .person-role {
    font-size: 27px;
    line-height: 1.1;
  }
</style>
</head>
<body>
  <section class="card card--front" aria-label="Card front">
    <div class="front-brand">
      <span class="front-brand-mark"></span>
      <span class="front-brand-name condensed">Quartz Hill Lane</span>
    </div>
    <div class="front-web condensed">quartzhilllane.net.au</div>
  </section>

  <section class="card card--back" aria-label="Card back">
    <div class="band band--brand">
      <span class="band-brand-name condensed">Quartz Hill Lane</span>
    </div>

    <ul class="contact-list condensed">
      <li>M: 0412 967 154</li>
      <li>P: 9735 6021</li>
      <li>E: nolan@quartzhilllane.net.au</li>
    </ul>

    <div class="band band--name">
      <div class="person">
        <div class="person-name">Nolan Pryce</div>
        <div class="person-role condensed">Director</div>
      </div>
    </div>
  </section>
</body>
</html>
```